Veldon Tracing, Inc. - Stationary Project
Business Cards and Stationary for Missing Person Consultants
Professional
Luke Hammond
Search Coordinator
718 West Marlow Avenue
Suite #263
Orlando, FL 32806
lhammond@veldontracing-demo.org
www.VeldonTracing-demo.org
Our organization is called upon
when someone disappears. We¹d like to have a professional business card that
is very eye-catching and people will notice. Please use the red, black and
gray colors in the logo to make a great looking business card, letterhead
and envelope. We look forward to seeing your designs.
We'd like to see a clever use of the logo on the back of the card in bigger format.
This is our logo in AI format.

```html
<!DOCTYPE html>
<html lang="en">
<head>
<meta charset="utf-8">
<title>Veldon Tracing – Business Card</title>
<link href="https://fonts.googleapis.com/css2?family=Source+Sans+3:wght@400;600;700&display=swap" rel="stylesheet">
<style>
  :root {
    --bg: #e8e5e1;
    --card: #ffffff;
    --red: #a3201f;
    --red-dark: #6e0e0e;
    --red-light: #d2463b;
    --ink: #1f1f1f;
    --text: #333333;
    --gray: #8a8a8a;
    --rule: #9a9a9a;
  }
  * { margin: 0; padding: 0; box-sizing: border-box; }
  html, body { width: 1200px; height: 965px; overflow: hidden; }
  body {
    background: var(--bg);
    font-family: "Source Sans 3", "Helvetica Neue", Arial, sans-serif;
    color: var(--text);
    position: relative;
  }
  .business-card {
    position: absolute;
    left: 100px; top: 245px;
    width: 1000px; height: 475px;
    background: var(--card);
    border-radius: 32px;
    overflow: hidden;
    border: 1px solid #d6d3cf;
  }
  .corner-swoosh { position: absolute; inset: 0; width: 100%; height: 100%; }
  .brand {
    position: absolute;
    left: 0; width: 1000px; top: 62px;
    display: flex; justify-content: center; align-items: center; gap: 22px;
  }
  .brand-mark {
    width: 86px; height: 86px; border-radius: 50%;
    background: var(--ink);
  }
  .brand-name {
    font-weight: 700; font-size: 78px; letter-spacing: 1px;
    color: var(--ink); line-height: 1;
  }
  .person {
    position: absolute; right: calc(1000px - 432px); top: 208px;
    text-align: right;
  }
  .person-name { font-weight: 700; font-size: 40px; color: var(--red); line-height: 1.05; }
  .person-title { font-weight: 700; font-size: 25px; color: var(--ink); margin-top: 4px; }
  .person-address { font-size: 25px; line-height: 1.35; margin-top: 28px; }
  .divider {
    position: absolute; left: 474px; top: 218px;
    width: 2px; height: 170px; background: var(--rule);
  }
  .contact-list {
    position: absolute; left: 530px; top: 222px;
    list-style: none;
  }
  .contact-list li {
    display: flex; align-items: center; gap: 12px;
    font-size: 25px; height: 42px;
  }
  .contact-list svg { width: 24px; height: 24px; flex: none; }
</style>
</head>
<body>
  <div class="business-card">
    <svg class="corner-swoosh" viewBox="0 0 1000 475" preserveAspectRatio="none" aria-hidden="true">
      <defs>
        <linearGradient id="shade" x1="0" y1="0" x2="1" y2="0">
          <stop offset="0" stop-color="#ffffff" stop-opacity="0"/>
          <stop offset="1" stop-color="#9d9d9d"/>
        </linearGradient>
        <linearGradient id="band" x1="0" y1="0" x2="0" y2="1">
          <stop offset="0" stop-color="#5c0a0a"/>
          <stop offset="0.5" stop-color="#8d1515"/>
          <stop offset="1" stop-color="#b22a24"/>
        </linearGradient>
      </defs>
      <path d="M770 0 C890 40 965 230 985 475 L1000 475 L1000 0 Z" fill="url(#shade)"/>
      <path d="M812 0 C925 45 985 230 1000 450 L1000 0 Z" fill="url(#band)"/>
      <path d="M812 0 C925 45 985 230 1000 450 L1000 380 C975 210 920 60 838 0 Z" fill="#d2463b" opacity="0.85"/>
    </svg>

    <div class="brand">
      <span class="brand-mark"></span>
      <span class="brand-name">Veldon Tracing</span>
    </div>

    <div class="person">
      <div class="person-name">Luke Hammond</div>
      <div class="person-title">Search Coordinator</div>
      <div class="person-address">718 West Marlow Avenue<br>Suite #263, Orlando, FL 32806</div>
    </div>

    <div class="divider"></div>

    <ul class="contact-list">
      <li>
        <svg viewBox="0 0 24 24"><rect x="7" y="2" width="10" height="20" rx="2" fill="var(--red)"/><rect x="9" y="5" width="6" height="9" fill="#fff"/></svg>
        (555) 418-2093
      </li>
      <li>
        <svg viewBox="0 0 24 24"><path d="M4 8 Q12 2 20 8 L18 10 L15 9 L15 7 Q12 6 9 7 L9 9 L6 10 Z" fill="var(--red)"/><rect x="5" y="12" width="14" height="9" rx="1.5" fill="var(--red)"/></svg>
        (555) 762-3158
      </li>
      <li>
        <svg viewBox="0 0 24 24"><circle cx="12" cy="12" r="9" fill="none" stroke="var(--red)" stroke-width="2.6"/><circle cx="12" cy="12" r="3.5" fill="none" stroke="var(--red)" stroke-width="2.6"/></svg>
        lhammond@veldontracing-demo.org
      </li>
      <li>
        <svg viewBox="0 0 24 24"><g fill="none" stroke="var(--red)" stroke-width="1.8"><circle cx="12" cy="12" r="9"/><ellipse cx="12" cy="12" rx="4" ry="9"/><path d="M3 12 H21 M5 7 H19 M5 17 H19"/></g></svg>
        www.VeldonTracing-demo.org
      </li>
    </ul>
  </div>
</body>
</html>
```